Pilates Studio webdesign - Homepage design

Need a web design for this new Pilates studio.

1) Need elegant design that has great use of stock photos. See attached plumeframe lightbox. Use these for your designs
http://www.frameplume.com/search/lightbox/58120947

Be creative in how you use images. Could be a collage, or single image if design is strong.

2) Also see attached site map (PDF)

3) Please refer to this website for the "rollover section" on homepage. https://www.bookingacademy-varn.com/
We want similar functionality for "I'm Here Because"

4) See attached logos ZIP file.

5) My client kind of likes this website too:
http://motionhallq.com

Target Market(s)

mostly women

Number of Pages Required

2 page

Font styles to use
Sans Serif

Requirements
Must have
• strong design
• good use of stock image(s)
• logo included
Nice to have
• elegant design
Should not have
• not planning to build a long scrolling page.

```html
<!DOCTYPE html>
<html lang="en">
<head>
<meta charset="utf-8">
<title>About Harlow – Corewell Studio</title>
<link rel="stylesheet" href="https://fonts.googleapis.com/css2?family=Source+Sans+3:ital,wght@0,300;0,400;0,600;0,700;1,300;1,400&display=swap">
<style>
  :root {
    --header-bg: #212121;
    --nav-active: #3d3d3d;
    --main-bg: #1b1b1b;
    --footer-bg: #262626;
    --bottom-bg: #1f1f1f;
    --blue: #4e6e8e;
    --orange: #f7941d;
    --white: #ffffff;
    --body-grey: #5a5a5a;
    --muted: #6a6a6a;
    --field-bg: #2d2d2d;
    --field-text: #7a7a7a;
    --rule: #444;
  }
  * { box-sizing: border-box; margin: 0; padding: 0; }
  html, body { width: 1200px; height: 1200px; overflow: hidden; }
  body { font-family: "Source Sans 3", sans-serif; background: var(--main-bg); position: relative; }

  .site-header { position: absolute; left: 0; top: 0; width: 1200px; height: 96px; background: var(--header-bg); }
  .brand { position: absolute; left: 67px; top: 19px; display: flex; align-items: center; gap: 12px; }
  .brand-mark { width: 58px; height: 58px; border-radius: 50%; background: var(--orange); }
  .brand-name { color: var(--blue); font-weight: 600; font-size: 21px; letter-spacing: 1px; text-transform: uppercase; }
  .main-nav a { position: absolute; top: 0; height: 96px; line-height: 98px; color: var(--white); text-decoration: none; font-weight: 300; font-size: 16.5px; white-space: nowrap; }
  .main-nav a.active { background: var(--nav-active); width: 162px; text-align: center; }

  .about { position: absolute; left: 0; top: 96px; width: 1200px; height: 718px; background: var(--main-bg); }
  .about-title { position: absolute; left: 60px; top: 58px; font-weight: 300; font-size: 80px; color: var(--white); line-height: 1; }
  .about-title span { color: var(--blue); }
  .title-rule { position: absolute; left: 67px; top: 154px; width: 60px; height: 1px; background: var(--rule); }
  .lead { position: absolute; left: 67px; top: 173px; width: 720px; font-style: italic; font-weight: 300; font-size: 27px; line-height: 23.5px; color: var(--blue); }
  .body-copy { position: absolute; left: 67px; top: 232px; width: 700px; font-weight: 300; font-size: 25.5px; line-height: 23.4px; color: var(--body-grey); }
  .body-copy p + p { margin-top: 23px; }
  .divider { position: absolute; left: 796px; top: 74px; width: 1px; height: 584px; background: var(--rule); }
  .feature { position: absolute; left: 829px; top: 106px; width: 299px; height: 552px; background: linear-gradient(180deg, #d8d8d8 0%, #8a8a8a 35%, #3a3a3a 65%, #0d0d0d 95%); }
  .feature-text { position: absolute; left: 18px; top: 358px; width: 275px; color: var(--white); }
  .feature-text h2 { font-weight: 700; font-size: 41px; line-height: 34px; }
  .feature-text p { margin-top: 8px; width: 262px; font-style: italic; font-size: 17px; line-height: 16.6px; }

  .site-footer { position: absolute; left: 0; top: 814px; width: 1200px; height: 346px; background: var(--footer-bg); }
  .studio-name { position: absolute; left: 67px; top: 40px; font-weight: 700; font-size: 17px; color: var(--blue); }
  .address { position: absolute; left: 67px; top: 62px; font-size: 13px; line-height: 14px; color: var(--blue); }
  .contact-item { position: absolute; left: 67px; display: flex; gap: 10px; align-items: flex-start; }
  .contact-item svg { width: 21px; height: 21px; flex: none; margin-top: 2px; }
  .contact-item b { display: block; color: var(--muted); font-weight: 600; font-size: 13px; line-height: 13px; }
  .contact-item span { color: var(--muted); font-weight: 300; font-size: 13px; line-height: 14px; }
  .social { position: absolute; left: 67px; top: 248px; display: flex; gap: 10px; }
  .social li { list-style: none; width: 29px; height: 29px; border-radius: 50%; background: var(--orange); }
  .col-heading { position: absolute; top: 40px; font-weight: 700; font-size: 17px; color: var(--blue); text-transform: uppercase; }
  .col-heading::before { content: "| "; font-weight: 400; }
  .field { position: absolute; left: 490px; width: 200px; height: 32px; background: var(--field-bg); color: var(--field-text); font-size: 13px; padding: 8px 12px; }
  .btn { position: absolute; background: var(--orange); color: var(--white); font-weight: 700; font-size: 13.5px; height: 32px; line-height: 32px; text-align: center; }
  .appt-copy { position: absolute; left: 926px; top: 67px; width: 206px; font-weight: 300; font-size: 13.5px; line-height: 13.5px; color: var(--muted); }

  .bottom-bar { position: absolute; left: 0; top: 1160px; width: 1200px; height: 40px; background: var(--bottom-bg); color: var(--muted); font-weight: 300; font-size: 13px; }
  .bottom-bar .copyright { position: absolute; left: 66px; top: 12px; }
  .bottom-bar .legal { position: absolute; right: 73px; top: 12px; }
</style>
</head>
<body>
  <header class="site-header">
    <div class="brand">
      <div class="brand-mark"></div>
      <div class="brand-name">Corewell Studio</div>
    </div>
    <nav class="main-nav">
      <a class="active" href="#" style="left:432px">ABOUT HARLOW</a>
      <a href="#" style="left:613px">WHAT IS COREWELL STUDIO</a>
      <a href="#" style="left:845px">SCHEDULING SESSIONS</a>
      <a href="#" style="left:1049px">REFERRALS</a>
    </nav>
  </header>

  <section class="about">
    <h1 class="about-title">About <span>Harlow</span></h1>
    <div class="title-rule"></div>
    <p class="lead">Lorem ipsum dolor sit amet, consectetur adipiscing elit.<br>Curabitur fringilla erat eu arcu pellentesque egestas.</p>
    <div class="body-copy">
      <p>Lorem ipsum dolor sit amet, consectetur adipiscing elit. Curabitur fringilla erat eu arcu pellentesque egestas. Ut sagittis ultrices tortor non placerat. Duis sodales lacus fermentum tellus tristique, quis laoreet magna posuere. Mauris ultrices, elit eu accumsan euismod, augue lectus ullamcorper libero, ut ullamcorper quam neque eu lorem. Pellentesque mattis lorem a diam elementum, at egestas urna egestas. Donec eleifend eu sem nec blandit. Ut a laoreet eros, tempor facilisis augue. Fusce eu vehicula massa, eget tempor erat. Aenean congue ultrices dui, nec posuere justo tempor ut. Ut vitae urna ultricies, varius quam vel, placerat ante. Vestibulum finibus nibh ut arcu vehicula porttitor. Nam interdum nisl eu magna viverra eleifend. Mauris erat ipsum, varius id feugiat vel, interdum id sem. Vivamus eget placerat ante. Donec quis tristique orci. Class aptent taciti sociosqu ad litora torquent per conubia nostra, per inceptos himenaeos.</p>
      <p>Morbi sollicitudin enim quis sollicitudin dictum. Fusce eu libero suscipit felis euismod pretium nec pretium est.</p>
    </div>
    <div class="divider"></div>
    <div class="feature" role="img" aria-label="Black and white photo of a man stretching his arms up against a wooden Pilates frame">
      <div class="feature-text">
        <h2>Lorem Ipsum Dolor Sit Amet</h2>
        <p>Lorem ipsum dolor sit amet, consectetur adipiscing elit. Curabitur fringilla erat eu arcu pellentesque egestas. Ut sagittis ultrices tortor non placerat.</p>
      </div>
    </div>
  </section>

  <footer class="site-footer">
    <div class="studio-name">Corewell Studio</div>
    <div class="address">1234 Street Name<br>Neighborhood, ST 5555, USA</div>

    <div class="contact-item" style="top:108px">
      <svg viewBox="0 0 24 24"><path fill="#f7941d" d="M20 15.5c-1.2 0-2.4-.2-3.6-.6-.3-.1-.7 0-1 .2l-2.2 2.2c-2.8-1.4-5.1-3.8-6.6-6.6l2.2-2.2c.3-.3.4-.7.3-1C8.7 6.4 8.5 5.2 8.5 4c0-.6-.4-1-1-1H4c-.6 0-1 .4-1 1 0 9.4 7.6 17 17 17 .6 0 1-.4 1-1v-3.5c0-.6-.4-1-1-1z" transform="scale(-1,1) translate(-24,0)"/></svg>
      <div><b>Phone</b><span>(123) 456-7890</span></div>
    </div>
    <div class="contact-item" style="top:155px">
      <svg viewBox="0 0 24 24"><path fill="#f7941d" d="M6 2h12v5H6zM3 8h18a2 2 0 0 1 2 2v7h-4v5H5v-5H1v-7a2 2 0 0 1 2-2zm4 8v4h10v-4z"/></svg>
      <div><b>Fax</b><span>(123) 456-7890</span></div>
    </div>
    <div class="contact-item" style="top:201px">
      <svg viewBox="0 0 24 24"><path fill="#f7941d" d="M2 5h20v14H2z"/><path fill="#262626" d="M2 5l10 7 10-7v2l-10 7L2 7z"/></svg>
      <div><b>Email</b><span>contact@corewellstudio.com</span></div>
    </div>
    <ul class="social" aria-label="Social links"><li></li><li></li><li></li><li></li></ul>

    <h3 class="col-heading" style="left:490px">Contact Us</h3>
    <div class="field" style="top:74px">Name</div>
    <div class="field" style="top:111px">Email</div>
    <div class="field" style="top:148px">Phone Number</div>
    <div class="field" style="top:185px;height:80px">Message</div>
    <div class="btn" style="left:490px;top:274px;width:95px">Submit</div>

    <h3 class="col-heading" style="left:926px">Make an Appointment</h3>
    <p class="appt-copy">Lorem ipsum dolor sit amet, consectetur adipiscing elit. Cras ut arcu ut erat aliquet ullamcorper. Vestibulum rutrum nunc dolor, et imperdiet ipsum finibus fermentum. Praesent quis ex vitae tellus ultrices eleifend.</p>
    <div class="btn" style="left:926px;top:176px;width:163px">Make Appointment</div>
  </footer>

  <div class="bottom-bar">
    <span class="copyright">Copyright © 2016 Corewell Studio. All rights reserved.</span>
    <span class="legal">Site Map | Privacy &amp; Legal</span>
  </div>
</body>
</html>
```